Glow and Petal med spa needs an awesome eye catching billboard ad

We need a billboard ad design for a Med Spa with location sin Brookhaven and Windermere FL A medical spa where the beauty of nature meets the power of science to treat the whole person, mind, body and soul.

Meadowlight Renewal Med Spa is a medical spa where the beauty of nature meets the power of science to create gorgeous, youthful looking skin. Located in Brookhaven, Florida, but also serving Four Corners, Celebration, and Windermere, Florida, the talented professional team brings decades of experience in world-class skin care to provide holistic, science-backed aesthetic services and health coaching.

Industry/Entity Type

Spa

Colors
fbee3e
fece3e
eea4c8
e667a6
fbee3d

Requirements
Must have
• Locations in Brookhaven and Lake Ardell
Phone 407-555-0192
website www.glowandpetal.example

Boards for each:
Aesthetic Treatments
Cosmetic Injectables
Lumora facial
add color vs too many earthtones, to catch the eye perhaps using yellow, something that catches the eye and stands out from the normal everyday
Thank you!!!!
Nice to have
• Boards for each:
Aesthetic Treatments
Cosmetic Injectables
Lumora facial
add color vs too many earthtones, to catch the eye
photos that match services,
Thank you!!!!

```html
<!DOCTYPE html>
<html lang="en">
<head>
<meta charset="utf-8">
<title>Meadowlight Renewal Med Spa – Aesthetic Treatments Billboard</title>
<link rel="stylesheet" href="https://fonts.googleapis.com/css2?family=Cinzel:wght@500;700&family=Marcellus&family=Sorts+Mill+Goudy&display=swap">
<style>
  :root {
    --backdrop: #4d4d4d;
    --paper: #ffffff;
    --pink: #e667a6;
    --yellow: #fbee3d;
    --sun: #fece3e;
    --orange: #f7941d;
    --gold: #c4ad7f;
    --ink: #161616;
  }
  html, body {
    margin: 0;
    width: 857px;
    height: 1200px;
    overflow: hidden;
    background: var(--backdrop);
  }
  .billboard {
    position: absolute;
    left: 28px;
    top: 400px;
    width: 800px;
    height: 400px;
    display: block;
    box-shadow: 0 6px 14px rgba(0,0,0,.45);
  }
  .brand-name { font-family: "Cinzel", serif; font-weight: 500; fill: var(--gold); }
  .headline { font-family: "Cinzel", serif; font-weight: 700; fill: var(--yellow); }
  .phone { font-family: "Marcellus", serif; fill: var(--ink); }
  .website { font-family: "Sorts Mill Goudy", serif; fill: var(--ink); }
  .locations { font-family: "Sorts Mill Goudy", serif; fill: var(--ink); }
</style>
</head>
<body>
<svg class="billboard" viewBox="0 0 1296 648" xmlns="http://www.w3.org/2000/svg">
  <defs>
    <linearGradient id="sunburst" x1="0" y1="0" x2="0" y2="1">
      <stop offset="0" stop-color="#f7941d"/>
      <stop offset=".4" stop-color="#fbb62f"/>
      <stop offset=".7" stop-color="#fece3e"/>
      <stop offset="1" stop-color="#fbee3d"/>
    </linearGradient>
    <linearGradient id="accent-orb" x1="0" y1="0" x2="1" y2="1">
      <stop offset="0" stop-color="#f7941d"/>
      <stop offset="1" stop-color="#fece3e"/>
    </linearGradient>
    <linearGradient id="treatment-photo" x1="0" y1="0" x2="1" y2="1">
      <stop offset="0" stop-color="#f1f1f1"/>
      <stop offset=".55" stop-color="#e9d6c8"/>
      <stop offset="1" stop-color="#d8d8d8"/>
    </linearGradient>
    <clipPath id="board"><rect width="1296" height="648"/></clipPath>
  </defs>

  <g clip-path="url(#board)">
    <rect class="board-paper" width="1296" height="648" fill="var(--paper)"/>

    <rect class="headline-band" x="600" y="195" width="696" height="217" fill="var(--pink)"/>
    <rect class="locations-band" x="600" y="565" width="696" height="83" fill="var(--sun)"/>

    <circle class="sun-arc" cx="160" cy="310" r="512" fill="url(#sunburst)"/>
    <circle class="sun-ring" cx="120" cy="330" r="475" fill="none" stroke="#fff6c0" stroke-width="3"/>

    <g role="img" aria-label="Photo of a woman lying on a treatment bed receiving a facial device treatment from a gloved aesthetician">
      <circle class="treatment-photo" cx="120" cy="330" r="450" fill="url(#treatment-photo)"/>
    </g>

    <circle class="accent-dot" cx="627" cy="130" r="22" fill="var(--sun)"/>
    <circle class="accent-dot" cx="661" cy="460" r="20" fill="var(--sun)"/>
    <circle class="accent-orb" cx="585" cy="605" r="48" fill="url(#accent-orb)"/>

    <circle class="brand-dot" cx="762" cy="88" r="16" fill="var(--gold)"/>
    <text class="brand-name" x="795" y="105" font-size="50" textLength="405" lengthAdjust="spacingAndGlyphs">MEADOWLIGHT</text>
    <text class="brand-name" x="997" y="142" font-size="20" letter-spacing="4" text-anchor="middle">RENEWAL MED SPA</text>

    <text class="headline" x="972" y="287" font-size="86" text-anchor="middle" textLength="457" lengthAdjust="spacingAndGlyphs">AESTHETIC</text>
    <text class="headline" x="972" y="375" font-size="86" text-anchor="middle" textLength="545" lengthAdjust="spacingAndGlyphs">TREATMENTS</text>

    <text class="phone" x="970" y="485" font-size="72" text-anchor="middle" textLength="420" lengthAdjust="spacingAndGlyphs">407-555-0192</text>
    <text class="website" x="970" y="535" font-size="36" text-anchor="middle" textLength="420" lengthAdjust="spacingAndGlyphs">www.glowandpetal.example</text>

    <text class="locations" x="959" y="613" font-size="33" text-anchor="middle" textLength="588" lengthAdjust="spacingAndGlyphs">Locations in Brookhaven and Lake Ardell</text>
  </g>
</svg>
</body>
</html>
```